Flyer für Vertrieb und Montage von Photovoltaikanlagen
Zielgruppe
Vertrieb und Montage von Photovoltaikanlagen für jeden Hausbesitzer
Aufgabenstellung
auf unsere WEB Site kann der Kunde sich vorab die Gesamtkosten der Anlage ausrechnen
ohne Angabe seine Identität preiszugeben

```html
<!DOCTYPE html>
<html lang="de">
<head>
<meta charset="utf-8">
<title>Birkenhain Solar – Flyer</title>
<link href="https://fonts.googleapis.com/css2?family=Open+Sans:wght@400;600;700;800&display=swap" rel="stylesheet">
<style>
  :root {
    --brand-blue: #1d5fae;
    --brand-blue-dark: #174e92;
    --text-dark: #2a2a2a;
    --text-grey: #8a8a8a;
    --paper: #f7f7f7;
    --backdrop: #d9d9d9;
    --sky-top: #7fb3e0;
    --sky-bottom: #dfeaf3;
    --roof: #7a5a4a;
  }
  * { box-sizing: border-box; margin: 0; padding: 0; }
  html, body { width: 1200px; height: 1200px; overflow: hidden; }
  body {
    background: var(--backdrop);
    font-family: "Open Sans", Arial, sans-serif;
    display: flex; align-items: center; justify-content: center; gap: 60px;
  }
  .flyer {
    position: relative;
    width: 440px; height: 940px;
    background: var(--paper);
    box-shadow: 0 10px 30px rgba(0,0,0,.12);
    overflow: hidden;
  }

  /* Wordmark */
  .wordmark { display: flex; align-items: center; gap: 12px; justify-content: center; }
  .wordmark__dot { width: 34px; height: 34px; border-radius: 50%; background: var(--brand-blue); }
  .wordmark__name {
    color: var(--brand-blue); font-weight: 700; font-size: 30px; letter-spacing: .5px; line-height: 1;
  }

  /* Front */
  .front__logo { height: 210px; display: flex; align-items: center; justify-content: center; }
  .front__photo {
    position: absolute; left: 50px; right: 0; top: 210px; height: 520px;
    background: linear-gradient(180deg, var(--sky-top) 0%, var(--sky-bottom) 28%, #9a8a80 45%, var(--roof) 100%);
  }
  .front__band {
    position: absolute; left: 50px; right: 30px; top: 610px; height: 96px;
    background: var(--brand-blue);
    display: flex; align-items: center; justify-content: center;
    color: #fff; font-weight: 700; font-size: 16px; letter-spacing: 1.4px; text-align: center;
    text-transform: uppercase; line-height: 1.5;
  }
  .front__band::after {
    content: ""; position: absolute; right: -18px; top: -18px; width: 5px; height: 96px; background: #fff;
  }
  .front__cta {
    position: absolute; right: 34px; top: 760px; display: flex; align-items: flex-start; gap: 16px;
  }
  .front__cta-text { text-align: right; font-weight: 700; font-size: 21px; color: var(--text-dark); line-height: 1.3; }
  .front__contact, .back__contact {
    position: absolute; right: 34px; bottom: 40px; text-align: right;
    font-size: 11.5px; color: var(--text-grey); line-height: 1.7;
  }

  /* Back */
  .back__photo {
    height: 260px;
    background: linear-gradient(160deg, #5f8fc7 0%, #274a7a 45%, #1a2f52 100%);
  }
  .back__body { padding: 40px 36px 0; }
  .back__headline { color: var(--brand-blue); font-weight: 800; font-size: 25px; line-height: 1.25; }
  .back__intro { margin-top: 12px; color: var(--text-grey); font-size: 14px; line-height: 1.5; }
  .benefits { list-style: none; margin-top: 34px; display: flex; flex-direction: column; gap: 34px; }
  .benefit { display: flex; gap: 18px; align-items: flex-start; }
  .benefit__icon {
    flex: none; width: 44px; height: 44px; border-radius: 50%; background: var(--brand-blue);
    display: flex; align-items: center; justify-content: center;
  }
  .benefit__title { font-weight: 700; font-size: 15px; color: var(--text-dark); }
  .benefit__text { margin-top: 4px; font-size: 12.5px; color: var(--text-grey); line-height: 1.5; }
  .back__footer { position: absolute; left: 0; right: 0; bottom: 120px; }
  .back__contact { text-align: center; left: 34px; }
</style>
</head>
<body>

  <!-- Front side -->
  <section class="flyer front">
    <div class="front__logo">
      <div class="wordmark">
        <span class="wordmark__dot"></span>
        <span class="wordmark__name">BIRKENHAIN SOLAR</span>
      </div>
    </div>
    <div class="front__photo" role="img" aria-label="Foto: Hausdach mit Photovoltaikmodulen, Schornstein und Dachfenster vor blauem Himmel"></div>
    <div class="front__band">Senken Sie Ihre Stromkosten<br>mit einer Photovoltaikanlage</div>
    <div class="front__cta">
      <p class="front__cta-text">Berechnen Sie jetzt<br>Ihre Gesamtkosten online!</p>
      <svg width="46" height="54" viewBox="0 0 46 54" aria-hidden="true">
        <rect x="2" y="2" width="42" height="50" rx="4" fill="none" stroke="var(--brand-blue)" stroke-width="3"/>
        <rect x="9" y="9" width="28" height="11" fill="none" stroke="var(--brand-blue)" stroke-width="2.5"/>
        <g fill="var(--brand-blue)">
          <rect x="9" y="26" width="7" height="6"/><rect x="19.5" y="26" width="7" height="6"/><rect x="30" y="26" width="7" height="6"/>
          <rect x="9" y="37" width="7" height="6"/><rect x="19.5" y="37" width="7" height="6"/><rect x="30" y="37" width="7" height="6"/>
        </g>
      </svg>
    </div>
    <address class="front__contact" style="font-style:normal">
      Adresse: Lindenweg 14, 24103 Kiel, Deutschland<br>
      E-Mail: kontakt@birkenhain-solar.de &nbsp;|&nbsp; Web: www.birkenhain-solar.de<br>
      Telefon: +49 431 550 2210 &nbsp;|&nbsp; +49 431 550 2211
    </address>
  </section>

  <!-- Back side -->
  <section class="flyer back">
    <div class="back__photo" role="img" aria-label="Foto: Monteur beim Installieren von Solarmodulen auf einem Dach"></div>
    <div class="back__body">
      <h2 class="back__headline">Sie denken über eine Photovoltaikanlage nach?</h2>
      <p class="back__intro">Nutzen Sie unseren Online-Rechner und überzeugen Sie sich von den Einsparungen.</p>
      <ul class="benefits">
        <li class="benefit">
          <span class="benefit__icon">
            <svg width="22" height="22" viewBox="0 0 22 22" aria-hidden="true"><path d="M3 11 L11 4 L19 11 V19 H3 Z" fill="none" stroke="#fff" stroke-width="2" stroke-linejoin="round"/></svg>
          </span>
          <div><p class="benefit__title">Zuverlässigkeit</p>
          <p class="benefit__text">Vertrauen Sie auf unsere Erfahrung – von der Beratung bis zur fertigen Photovoltaikanlage.</p></div>
        </li>
        <li class="benefit">
          <span class="benefit__icon">
            <svg width="22" height="22" viewBox="0 0 22 22" aria-hidden="true"><path d="M4 9 A7 7 0 0 1 17 7 M18 13 A7 7 0 0 1 5 15" fill="none" stroke="#fff" stroke-width="2"/><path d="M17 3 V7 H13 M5 19 V15 H9" fill="none" stroke="#fff" stroke-width="2"/></svg>
          </span>
          <div><p class="benefit__title">Effizienz</p>
          <p class="benefit__text">Unsere Photovoltaikanlagen arbeiten effizient und langlebig.</p></div>
        </li>
        <li class="benefit">
          <span class="benefit__icon">
            <svg width="22" height="22" viewBox="0 0 22 22" aria-hidden="true"><circle cx="11" cy="11" r="8" fill="none" stroke="#fff" stroke-width="2"/><path d="M14 7.5 A4 4 0 1 0 14 14.5 M6 10 H12 M6 12.5 H12" fill="none" stroke="#fff" stroke-width="1.8"/></svg>
          </span>
          <div><p class="benefit__title">Geld sparen</p>
          <p class="benefit__text">Machen Sie sich unabhängig und senken Sie Ihre Stromkosten dauerhaft.</p></div>
        </li>
      </ul>
    </div>
    <div class="back__footer">
      <div class="wordmark">
        <span class="wordmark__dot"></span>
        <span class="wordmark__name">BIRKENHAIN SOLAR</span>
      </div>
    </div>
    <address class="back__contact" style="font-style:normal">
      Adresse: Lindenweg 14, 24103 Kiel, Deutschland<br>
      E-Mail: kontakt@birkenhain-solar.de &nbsp;|&nbsp; Web: www.birkenhain-solar.de<br>
      Telefon: +49 431 550 2210 &nbsp;|&nbsp; +49 431 550 2211
    </address>
  </section>

</body>
</html>
```